Corvane Optics PowerPoint Template

Corvane Optics needs a nice new corporate PowerPoint template, to be used for all types of presentations: sales, business development, finance, board/exec, etc.

I'd like to get a clean layout that reflects the brand (www.corvaneoptics.example), has a bright, interesting title slide, and then minimal graphics on the content slides. Ideally the content slides would have a header, "co" circle part of the Corvane Optics logo (either above or below), copyright/confidential footer, and page #.

About us: we have developed a revolutionary new array camera for mobile devices, providing depth at every pixel. Focus on any subject, change focus (even on multiple subjects) after you take the photo, capture linear measurements, scale and segment your images, change backgrounds, and apply filters, all from any device.
It's not just about megapixels anymore.
See www.corvaneoptics.example for info.

Target Market(s)

The audience for 90% of our presentations is highly educated executives at technology companies.

Industry/Entity Type

Camera

Requirements
Nice to have
• It would be great to show an image in a phone UI on the title slide, similar to the approach on our website.
Helpful to have tagline on title slide: "A smart camera for your smartphone." It may also fit on the content slides - feel free to try.
I attached a product photo, but using it is completely optional.
I'd like the "co" circle on the content slides, but the whole logo on the title slides.
Thanks!

```html
<!DOCTYPE html>
<html lang="en">
<head>
<meta charset="utf-8">
<title>Corvane Optics – Presentation Template</title>
<link rel="stylesheet" href="https://fonts.googleapis.com/css2?family=Carlito:wght@400;700&family=Arimo:wght@700&display=swap">
<style>
  :root {
    --navy: #0f4a68;
    --yellow: #f7c824;
    --white: #ffffff;
    --ink: #1a1a1a;
    --muted: #b48f1e;
    --frame: #bdbdbd;
    --page: #ffffff;
    --screen-tone: #b09a78;
    --photo-tone-a: #8fb0cf;
    --photo-tone-b: #6d93bd;
  }
  * { box-sizing: border-box; margin: 0; padding: 0; }
  html, body { width: 1200px; height: 499px; overflow: hidden; background: var(--page); }
  body { position: relative; font-family: "Carlito", "Calibri", sans-serif; color: var(--ink); }

  .slide {
    position: absolute;
    background: var(--white);
    border: 1px solid var(--frame);
    overflow: hidden;
  }
  .slide--title { left: 46px; top: 42px; width: 539px; height: 404px; }
  .slide--content { left: 603px; top: 44px; width: 543px; height: 404px; }

  /* Title slide */
  .brand { position: absolute; left: 16px; top: 18px; display: flex; align-items: center; gap: 6px; }
  .brand__dot { width: 24px; height: 24px; border-radius: 50%; background: var(--navy); }
  .brand__name { font-weight: 700; font-size: 22px; color: var(--navy); letter-spacing: -0.2px; }

  .phone {
    position: absolute; left: 16px; top: 70px; width: 350px; height: 182px;
    border-radius: 14px;
    background: linear-gradient(#2a2a2a, #0c0c0c);
  }
  .phone__screen {
    position: absolute; left: 44px; top: 18px; width: 258px; height: 144px;
    background: var(--screen-tone);
  }
  .phone__keys { position: absolute; left: 318px; top: 22px; width: 18px; height: 138px; }

  .tagline {
    font-family: "Arimo", "Arial", sans-serif; font-weight: 700; color: var(--ink);
    line-height: 1.15;
  }
  .slide--title .tagline { position: absolute; left: 383px; top: 146px; font-size: 13px; }

  .title-band {
    position: absolute; left: 0; top: 274px; width: 100%; height: 130px; background: var(--yellow);
  }
  .title-band__frame { position: absolute; left: 14px; top: 10px; width: 511px; height: 112px; }
  .title-band__heading { position: absolute; left: 50px; top: 48px; font-size: 22px; font-weight: 700; color: var(--ink); }
  .title-band__sub { position: absolute; left: 50px; top: 91px; font-size: 14px; font-weight: 400; color: var(--muted); }

  /* Content slide */
  .header-band { position: absolute; left: 0; top: 0; width: 100%; height: 54px; background: var(--navy); }
  .header-band__frame { position: absolute; left: 8px; top: 4px; width: 527px; height: 46px; }
  .header-band__title { position: absolute; left: 24px; top: 13px; font-size: 22px; font-weight: 400; color: var(--white); }

  .bullets { position: absolute; left: 26px; top: 63px; width: 300px; list-style: none; }
  .bullets li { position: relative; line-height: 17px; }
  .bullets > li { font-size: 14px; padding-left: 19px; margin-bottom: 4px; }
  .bullets > li::before { content: "•"; position: absolute; left: 2px; color: var(--yellow); }
  .bullets ul { list-style: none; margin-top: 4px; }
  .bullets ul li { font-size: 12.5px; padding-left: 24px; margin-bottom: 4px; }
  .bullets ul li::before { content: "–"; position: absolute; left: 5px; color: var(--yellow); }

  .photo {
    position: absolute; left: 353px; width: 142px; height: 96px;
    border: 4px solid var(--white); box-shadow: 0 0 0 1px #d6d6d6;
    background: linear-gradient(180deg, var(--photo-tone-a), var(--photo-tone-b));
  }
  .photo--1 { top: 60px; }
  .photo--2 { top: 167px; }
  .photo--3 { top: 274px; }

  .slide--content .tagline { position: absolute; left: 11px; top: 366px; font-size: 9.5px; line-height: 1.1; }
  .mark-dot { position: absolute; left: 509px; top: 362px; width: 24px; height: 24px; border-radius: 50%; background: var(--navy); }

  .footer-band {
    position: absolute; left: 0; top: 391px; width: 100%; height: 13px; background: var(--yellow);
    font-size: 8px; color: var(--white); line-height: 13px;
  }
  .footer-band__note { position: absolute; left: 0; width: 100%; text-align: center; }
  .footer-band__page { position: absolute; left: 476px; }
</style>
</head>
<body>

<section class="slide slide--title">
  <div class="brand">
    <span class="brand__dot"></span>
    <span class="brand__name">Corvane Optics</span>
  </div>

  <div class="phone">
    <div class="phone__screen" role="img" aria-label="Camera viewfinder showing a youth baseball game"></div>
    <svg class="phone__keys" viewBox="0 0 18 138" fill="none" stroke="#9a9a9a" stroke-width="1.6" aria-hidden="true">
      <circle cx="8" cy="8" r="4.5"/><line x1="11" y1="11" x2="15" y2="15"/>
      <path d="M3 52 L9 46 L15 52 M5 51 V57 H13 V51"/>
      <line x1="7" y1="86" x2="7" y2="96"/><line x1="10" y1="86" x2="10" y2="96"/><line x1="13" y1="86" x2="13" y2="96"/>
      <path d="M13 124 A5 5 0 1 1 6 122 M6 118 V123 H11"/>
    </svg>
  </div>

  <p class="tagline">A Smart Camera<br>for Your Smartphone</p>

  <div class="title-band">
    <svg class="title-band__frame" viewBox="0 0 511 112" fill="none" stroke="#ffffff" stroke-width="3" aria-hidden="true">
      <path d="M2 22 V6 Q2 2 6 2 H24"/>
      <path d="M487 2 H505 Q509 2 509 6 V22"/>
      <path d="M2 90 V106 Q2 110 6 110 H24"/>
      <path d="M487 110 H505 Q509 110 509 106 V90"/>
    </svg>
    <h1 class="title-band__heading">Lorem ipsum dolor sit amet</h1>
    <p class="title-band__sub">Suspendisse euismod libero quis quam varius lobortis</p>
  </div>
</section>

<section class="slide slide--content">
  <div class="header-band">
    <svg class="header-band__frame" viewBox="0 0 527 46" fill="none" stroke="#ffffff" stroke-width="2.5" aria-hidden="true">
      <path d="M2 14 V5 Q2 2 5 2 H16"/>
      <path d="M2 32 V41 Q2 44 5 44 H16"/>
      <path d="M511 2 H522 Q525 2 525 5 V14"/>
      <path d="M511 44 H522 Q525 44 525 41 V32"/>
    </svg>
    <h2 class="header-band__title">Lorem ipsum dolor sit amet consectetur</h2>
  </div>

  <ul class="bullets">
    <li>Lorem ipsum dolor sit amet,<br>consectetur adipiscing elit.
      <ul>
        <li>Integer cursus augue ut tristique<br>pellentesque.</li>
        <li>Suspendisse euismod libero quis<br>quam varius lobortis.</li>
      </ul>
    </li>
    <li>Morbi malesuada vulputate tortor nec<br>faucibus.
      <ul>
        <li>Phasellus quis commodo justo. Nunc<br>rutrum lorem vitae odio eleifend<br>mattis.</li>
        <li>Nullam eleifend urna molestie<br>consequat mollis.</li>
      </ul>
    </li>
    <li>Donec sagittis enim at lorem tristique<br>laoreet. Vestibulum ante ipsum primis</li>
  </ul>

  <div class="photo photo--1" role="img" aria-label="Portrait photo in front of a suspension bridge, first focus setting"></div>
  <div class="photo photo--2" role="img" aria-label="Same portrait photo, second focus setting"></div>
  <div class="photo photo--3" role="img" aria-label="Same portrait photo, third focus setting"></div>

  <p class="tagline">A Smart Camera<br>for Your Smartphone</p>
  <span class="mark-dot" aria-hidden="true"></span>

  <footer class="footer-band">
    <span class="footer-band__note">Confidential</span>
    <span class="footer-band__page">2</span>
  </footer>
</section>

</body>
</html>
```